Flyer-Design für Apotheke
Zielgruppe
Wir sind eine Apotheke, mit Schwerpunkt Mutter-Kind / Wiegenhafen Apotheke (www.wiegenhafen Apotheke)
Zielgruppe: Wir haben uns zertifiziert und spezialisiert im Bereich Mütter / Kinderwunsch / Stillen / Babys etc. (Siehe Anbei unser aktueller Entwurf Mutter-Kind-Broschüre)
Wir haben zahlreiche Handouts zu spezifischen Themen von der LHTV und unserem Verein Wiegenhafen Apotheken für unser Kunden schon fertig gestellt (siehe ein Beispiel im Anhang, auf dem wir noch unser Logo eingefügt haben).
Die Handouts sind meist 4-seitig A5, im Anhang mit unserem Logo noch versehen.
Zu zwei Themen möchten wir jetzt noch selbst ein Handout erstellen.
1) Fieberthermometer
2) Schnuller
Ziel: 4-6 Seiten, wir wollen es dann bei Druckfuchs drucken lassen.
Zielgruppe: Mütter, die zu uns in die Apotheke kommen und beraten werden (konkret in diesen Beispielen zum Thema Fieberthermometer bzw. Schnuller. Damit sie was mit nach Hause nehmen können, möchten wir die Handouts erstellen.
Texte anbei, Graphische Umsetzung ggf. mit netten Baby/Mütterbildern o.ä. erwünscht
Aufgabenstellung
Einbau Logo Tolvena-Apotheke (siehe Anhang) ähnlich wie auf dem Flyer Ernährung
(als Logo ohne Adresse etc. und irgendwo unter mit Adresse, Telefon etc.)
Logo Wiegenhafen Apotheke DARF NICHT MIT DRAUF

```html
<!DOCTYPE html>
<html lang="de">
<head>
<meta charset="utf-8">
<title>Der Schnuller – ja oder nein? · Informationsbroschüre</title>
<link href="https://fonts.googleapis.com/css2?family=Open+Sans:wght@400;600;700&family=Dancing+Script:wght@500&display=swap" rel="stylesheet">
<style>
  :root{
    --stage:#9fcbd8;
    --paper:#ffffff;
    --teal:#2aa3bf;
    --teal-dark:#1c8aa6;
    --teal-soft:#6cc0d4;
    --sky-top:#d7ecf3;
    --sky-bottom:#5fb3cb;
    --ink:#3a3f44;
    --ink-soft:#7a8288;
    --navy:#2b3f6b;
    --photo-warm:#d9c4c0;
    --photo-cool:#c9dbe6;
  }
  *{box-sizing:border-box;margin:0;padding:0}
  html,body{width:997px;height:1200px;overflow:hidden}
  body{background:var(--stage);font-family:"Open Sans",Arial,sans-serif;color:var(--ink);position:relative}

  .page{position:absolute;background:var(--paper);overflow:hidden;box-shadow:0 4px 14px rgba(30,70,90,.18)}
  .sky{background:linear-gradient(180deg,var(--sky-top) 0%,#a6d4e3 45%,var(--sky-bottom) 100%)}
  .photo{position:absolute}

  /* back page */
  .back{left:48px;top:30px;width:420px;height:560px}
  .back-top{position:absolute;left:0;top:0;width:100%;height:300px}
  .tips-frame{position:absolute;left:20px;top:26px;width:380px;height:256px;border:9px solid var(--teal);background:var(--paper);padding:11px 12px 10px;display:flex;flex-direction:column}
  .tips-title{font-size:9.5px;font-weight:700;color:var(--teal);margin-bottom:7px}
  .tips-cols{display:flex;gap:14px}
  .tips-cols ul{flex:1;list-style:none;font-size:8.2px;line-height:1.32}
  .tips-cols li{position:relative;padding-left:8px;margin-bottom:3px}
  .tips-cols li::before{content:"•";position:absolute;left:0}
  .tips-note{font-size:8.2px;margin-top:6px}
  .signature{font-family:"Dancing Script",cursive;font-size:13px;color:var(--navy);margin-top:auto;white-space:nowrap;text-align:right}
  .brand{font-weight:700;font-size:19px;line-height:1;color:var(--ink);display:flex;align-items:center;gap:6px}
  .brand-dot{width:9px;height:9px;border-radius:50%;background:var(--teal)}
  .back .brand{position:absolute;left:36px;top:336px}
  .contact{position:absolute;left:36px;top:376px;font-size:9.5px;line-height:1.5}
  .contact b{font-weight:700}
  .disclaimer{position:absolute;left:36px;top:438px;width:330px;font-size:6.5px;color:var(--ink-soft);line-height:1.4}
  .web-band{position:absolute;left:0;bottom:0;width:100%;height:34px;background:linear-gradient(90deg,var(--teal-soft),var(--teal));color:#e8f6fa;font-size:9px;font-weight:600;display:flex;align-items:center;justify-content:center}

  /* front cover */
  .front{left:528px;top:30px;width:420px;height:560px}
  .front-photo{left:0;top:0;width:100%;height:300px;background:linear-gradient(135deg,var(--photo-cool),#ece4e6 50%,var(--photo-warm))}
  .front-sky{position:absolute;left:0;top:300px;width:100%;height:260px}
  .title-bar{position:absolute;left:20px;top:330px;background:var(--teal);color:#fff;font-size:18px;font-weight:700;padding:6px 14px}
  .subtitle-bar{position:absolute;left:20px;top:370px;background:var(--teal-soft);color:#fff;font-size:12px;padding:4px 12px}
  .front-address{position:absolute;left:20px;top:462px;font-size:8px;color:#fff;line-height:1.5}
  .front .brand-box{position:absolute;right:20px;bottom:26px;background:var(--paper);padding:10px 12px}
  .front .brand{font-size:15px}

  /* inner spread */
  .spread-left{left:48px;top:618px;width:450px;height:550px}
  .spread-right{left:498px;top:618px;width:450px;height:550px;border-left:1px solid #e3e8ea}
  .photo-mom{left:30px;top:26px;width:390px;height:180px;background:linear-gradient(120deg,#e4d3c8,#f1ece8 55%,#d9e6ee)}
  .photo-sleep{left:60px;top:36px;width:360px;height:170px;background:linear-gradient(120deg,#f4f6f8,#dce9f2 60%,#a9c9e4)}
  .photo-pacifiers{left:270px;top:400px;width:150px;height:100px;background:linear-gradient(135deg,#f6dbe3,#fdf2d2 50%,#cde6f5)}
  .intro{position:absolute;left:30px;top:222px;width:390px;font-size:8px;line-height:1.45}
  .cols{position:absolute;left:30px;top:262px;width:390px;display:flex;gap:18px}
  .right-cols{left:30px;top:222px;width:390px}
  .col{flex:1}
  .col h3{font-size:10px;font-weight:600;color:var(--teal);margin-bottom:4px}
  .col ul{list-style:none;font-size:7.6px;line-height:1.45}
  .col li{position:relative;padding-left:8px;margin-bottom:3px}
  .col li::before{content:"•";position:absolute;left:0}
  .footnote{position:absolute;left:30px;bottom:48px;width:390px;font-size:6.5px;color:var(--ink-soft)}
</style>
</head>
<body>

<section class="page back" aria-label="Rückseite">
  <div class="back-top sky">
    <div class="tips-frame">
      <p class="tips-title">Wertvolle Tipps beim Umgang mit dem Beruhigungssauger:</p>
      <div class="tips-cols">
        <ul>
          <li>In den <b>ersten 4-6 Wochen</b> möglichst den Gebrauch <b>vermeiden</b>, um die Milchproduktion optimal anregen zu lassen</li>
          <li>Schnuller ist kein Ersatz für engen Körperkontakt und Stillen</li>
          <li>Kein Dauergebrauch, nur <b>kurzzeitige Anwendung</b></li>
          <li>Falls Schnuller beim Schlafen herausfällt, nicht wieder zurück in den Mund schieben</li>
        </ul>
        <ul>
          <li>Schnuller nicht herumliegen lassen, so wird das Kind dazu verleitet</li>
          <li>Sprechen ohne Beruhigungssauger</li>
          <li>Ab dem <b>2. Lebensjahr</b> mit dem <b>Abgewöhnen</b> beginnen</li>
          <li>Auf hygienischen Umgang achten</li>
        </ul>
      </div>
      <p class="tips-note">Bei weiteren Fragen helfen wir Ihnen gerne weiter.</p>
      <p class="signature">Ihr babyfreundliches Team der Tolvena Apotheke Lindhoven</p>
    </div>
  </div>
  <div class="brand"><span>Tolvena Apotheke</span><span class="brand-dot"></span></div>
  <p class="contact">Kastanienweg 8 · 47110 Lindhoven · <b>Tel.</b> 04711 5520310<br><b>Fax</b> 5520311 · tolvena@lindhoven-apotheken.de<br><b>www.lindhoven-apotheken.de</b></p>
  <p class="disclaimer">Die vorliegenden Informationen ersetzen keine persönliche Beratung durch Ihre Apotheke oder Ihren Kinderarzt.</p>
  <div class="web-band">www.lindhoven-apotheken.de</div>
</section>

<section class="page front" aria-label="Titelseite">
  <div class="photo front-photo" role="img" aria-label="Foto: Mutter hält ihr Baby mit Schnuller liebevoll im Arm"></div>
  <div class="front-sky sky"></div>
  <h1 class="title-bar">Der Schnuller – ja oder nein?</h1>
  <p class="subtitle-bar">Informationsbroschüre</p>
  <p class="front-address">Kastanienweg 8 · 47110 Lindhoven · Tel. 04711 5520310<br>Fax 5520311 · tolvena@lindhoven-apotheken.de</p>
  <div class="brand-box"><div class="brand"><span>Tolvena Apotheke</span><span class="brand-dot"></span></div></div>
</section>

<section class="page spread-left" aria-label="Innenseite links">
  <div class="photo photo-mom" role="img" aria-label="Foto: lächelnde Mutter mit Baby"></div>
  <p class="intro">Der Schnuller ist für viele Eltern ein treuer Helfer. Doch er hat Vor- und Nachteile, die man kennen sollte, bevor man ihn dem Baby anbietet.</p>
  <div class="cols">
    <div class="col">
      <h3>Was spricht dafür?</h3>
      <ul>
        <li>Der Saugreflex wird befriedigt und das Baby beruhigt sich schneller.</li>
        <li>Schnuller können helfen, Daumenlutschen zu vermeiden.</li>
        <li>Er kann das Einschlafen erleichtern und Trost spenden.</li>
        <li>Studien deuten auf ein geringeres Risiko beim plötzlichen Kindstod hin.</li>
      </ul>
    </div>
    <div class="col">
      <h3>Was spricht dagegen?</h3>
      <ul>
        <li>Frühes Saugen am Schnuller kann das Stillen stören.</li>
        <li>Zu häufige Nutzung kann Zähne und Kiefer verformen.</li>
        <li>Die Sprachentwicklung kann verzögert werden.</li>
        <li>Mittelohrentzündungen treten häufiger auf.</li>
        <li>Eine Abhängigkeit vom Schnuller kann entstehen.</li>
      </ul>
    </div>
  </div>
  <p class="footnote">Quelle: Empfehlungen der Stillberatung, Stand 2016.</p>
  <div class="web-band">www.lindhoven-apotheken.de</div>
</section>

<section class="page spread-right" aria-label="Innenseite rechts">
  <div class="photo photo-sleep" role="img" aria-label="Foto: schlafendes Baby im hellblauen Strampler"></div>
  <div class="cols right-cols">
    <div class="col">
      <h3>Anforderungen an den Schnuller:</h3>
      <ul>
        <li><b>Material:</b> Silikon ist geruchlos und leicht zu reinigen.</li>
        <li>Naturkautschuk ist weicher, altert aber schneller.</li>
        <li><b>Größe:</b> passend zum Alter des Kindes wählen.</li>
        <li><b>Form:</b> kiefergerecht und flach geformt.</li>
        <li><b>Tipp:</b> Schnuller regelmäßig auf Risse prüfen und rechtzeitig ersetzen.</li>
        <li><b>Achtung:</b> Schnullerketten nur kurz und unter Aufsicht verwenden.</li>
      </ul>
    </div>
    <div class="col">
      <h3>&nbsp;</h3>
      <ul>
        <li>Schnuller täglich mit heißem Wasser reinigen, nie ablecken.</li>
        <li>Beim Kauf auf Luftlöcher im Schild achten.</li>
        <li>Ersatzschnuller bereithalten, um Hektik zu vermeiden.</li>
      </ul>
    </div>
  </div>
  <div class="photo photo-pacifiers" role="img" aria-label="Foto: zwei Schnuller in Rosa und Blau"></div>
  <p class="footnote">Alle Angaben ohne Gewähr, bei Fragen beraten wir Sie gern.</p>
  <div class="web-band">www.lindhoven-apotheken.de</div>
</section>

</body>
</html>
```